Post card Design 99mm x 210mm

Holiday Park, units, tent sites, powered sites for caravans and motor homes. Flyer needed to distribute to Information centres and other tourist attractions around the country to advertise the Park. I have a logo and the photo of the Kaipara harbour that is on the web site. please advise what else you require

Tourist

```html
<!DOCTYPE html>
<html lang="en">
<head>
<meta charset="utf-8">
<title>Tidewater Holiday Park – Cabins and Camping</title>
<link rel="stylesheet" href="https://fonts.googleapis.com/css2?family=Arimo:wght@400&family=Lato:wght@700;900&family=Oswald:wght@600&display=swap">
<style>
  :root {
    --park-blue: #0b4f9e;
    --sky-blue: #5db5e4;
    --sun-yellow: #f5b324;
    --leaf-green: #66b845;
    --leaf-green-deep: #4ea53a;
    --ink-navy: #173f7c;
    --ink-dark: #2b2b2b;
    --paper: #ffffff;
  }
  * { box-sizing: border-box; margin: 0; padding: 0; }
  html, body { width: 880px; height: 1200px; overflow: hidden; background: #ececec; }
  .flyer {
    position: relative;
    width: 880px;
    height: 1200px;
    background: var(--paper);
    overflow: hidden;
    font-family: "Lato", Arial, sans-serif;
  }
  .flyer__shapes { position: absolute; inset: 0; }

  .brand {
    position: absolute;
    left: 86px;
    top: 100px;
    display: flex;
    align-items: center;
    gap: 16px;
    color: var(--paper);
    font-family: "Arimo", Arial, sans-serif;
    font-weight: 400;
  }
  .brand__dot { width: 58px; height: 58px; border-radius: 50%; background: var(--sun-yellow); }
  .brand__name { font-size: 34px; line-height: 36px; }

  .tagline {
    position: absolute;
    left: 560px;
    top: 338px;
    color: var(--paper);
    font-family: "Arimo", Arial, sans-serif;
    line-height: 1;
  }
  .tagline__big { font-size: 46px; letter-spacing: -1px; }
  .tagline__small { font-size: 26px; }
  .tagline__second { display: block; font-size: 46px; margin-left: 108px; margin-top: -10px; }

  .headline {
    position: absolute;
    left: 44px;
    top: 740px;
    font-family: "Arimo", Arial, sans-serif;
    font-weight: 400;
    line-height: 1;
  }
  .headline__main { display: block; color: var(--park-blue); font-size: 122px; letter-spacing: 2px; }
  .headline__sub { display: block; color: var(--ink-dark); font-size: 55px; letter-spacing: 1px; margin-top: 14px; }

  .facilities {
    position: absolute;
    left: 586px;
    top: 510px;
    width: 290px;
  }
  .facilities__title {
    font-family: "Oswald", "Arial Narrow", sans-serif;
    font-weight: 600;
    font-size: 52px;
    line-height: 1;
    color: var(--paper);
    letter-spacing: 1px;
    margin-left: 6px;
  }
  .facilities__list { list-style: none; margin-top: 26px; }
  .facilities__item {
    position: relative;
    padding-left: 24px;
    font-size: 21px;
    font-weight: 700;
    line-height: 29px;
    color: var(--ink-navy);
  }
  .facilities__item::before {
    content: "";
    position: absolute;
    left: 2px;
    top: 10px;
    width: 9px;
    height: 9px;
    border-radius: 50%;
    background: var(--sun-yellow);
  }

  .social {
    position: absolute;
    left: 48px;
    top: 1008px;
    display: flex;
    align-items: center;
    gap: 20px;
  }
  .social__label { font-size: 24px; font-weight: 700; color: var(--ink-dark); margin-right: 4px; }
  .social__mark { width: 40px; height: 40px; border-radius: 6px; }
  .social__mark--one { background: #3b5a9a; }
  .social__mark--two { background: #3fb5e6; }

  .contact {
    position: absolute;
    right: 30px;
    top: 1066px;
    text-align: right;
    color: var(--paper);
    font-size: 24px;
    font-weight: 700;
  }
  .contact__line {
    display: flex;
    justify-content: flex-end;
    align-items: center;
    gap: 10px;
    height: 40px;
  }
  .contact__icon { width: 20px; height: 20px; flex: none; }
</style>
</head>
<body>
<main class="flyer">
  <svg class="flyer__shapes" width="880" height="1200" viewBox="0 0 880 1200" xmlns="http://www.w3.org/2000/svg">
    <defs>
      <linearGradient id="harbourGrad" x1="0" y1="0" x2="0" y2="1">
        <stop offset="0" stop-color="#3c78c8"/>
        <stop offset="0.45" stop-color="#7fa7c9"/>
        <stop offset="0.6" stop-color="#3f6f36"/>
        <stop offset="1" stop-color="#9cb27a"/>
      </linearGradient>
      <linearGradient id="shoreGrad" x1="0" y1="0" x2="0" y2="1">
        <stop offset="0" stop-color="#4b8bb6"/>
        <stop offset="0.35" stop-color="#5fa8c9"/>
        <stop offset="0.7" stop-color="#6fb6d0"/>
        <stop offset="1" stop-color="#3d5a2a"/>
      </linearGradient>
      <linearGradient id="panelGrad" x1="0" y1="0" x2="1" y2="1">
        <stop offset="0" stop-color="var(--leaf-green)"/>
        <stop offset="1" stop-color="var(--leaf-green-deep)"/>
      </linearGradient>
    </defs>

    <!-- top photo: harbour view -->
    <path role="img" aria-label="Photo of the harbour with trees on the shoreline"
          d="M255 262 C300 215 340 175 380 145 C520 62 700 42 880 70 V452 C720 472 540 440 420 382 C340 338 290 300 255 262 Z"
          fill="url(#harbourGrad)"/>
    <path d="M255 262 C290 300 340 338 420 382 C540 440 720 472 880 452" fill="none" stroke="var(--sun-yellow)" stroke-width="10" transform="translate(0,10)"/>
    <path d="M255 262 C290 300 340 338 420 382 C540 440 720 472 880 452" fill="none" stroke="var(--sky-blue)" stroke-width="6" transform="translate(0,24)"/>

    <!-- header band -->
    <path class="header-band" d="M0 0 H880 V70 C700 42 520 62 380 145 C280 205 150 242 0 238 Z" fill="var(--park-blue)"/>
    <path d="M0 238 C150 242 280 205 380 145 C520 62 700 42 880 70" fill="none" stroke="var(--sky-blue)" stroke-width="6" transform="translate(0,6)"/>
    <path d="M0 238 C150 242 280 205 380 145 C520 62 700 42 880 70" fill="none" stroke="var(--sun-yellow)" stroke-width="9" transform="translate(0,16)"/>

    <!-- left photo: shoreline and palms -->
    <path d="M0 345 C160 330 320 420 385 640 C280 690 120 690 0 670 Z" fill="none" stroke="var(--sky-blue)" stroke-width="26"/>
    <path d="M0 345 C160 330 320 420 385 640 C280 690 120 690 0 670 Z" fill="none" stroke="var(--paper)" stroke-width="18"/>
    <path d="M0 345 C160 330 320 420 385 640 C280 690 120 690 0 670 Z" fill="none" stroke="var(--sun-yellow)" stroke-width="11"/>
    <path role="img" aria-label="Photo of calm harbour water with palm fronds in the foreground"
          d="M0 345 C160 330 320 420 385 640 C280 690 120 690 0 670 Z" fill="url(#shoreGrad)"/>

    <!-- facilities panel -->
    <path d="M600 478 H880 V968 H620 Q550 968 550 898 V528 Q550 478 600 478 Z" fill="url(#panelGrad)"/>

    <!-- footer band -->
    <path d="M0 1124 C280 1112 560 1042 880 1016" fill="none" stroke="var(--leaf-green)" stroke-width="8"/>
    <path d="M0 1142 C260 1132 580 1068 880 1040 V1200 H0 Z" fill="var(--park-blue)"/>
  </svg>

  <div class="brand">
    <span class="brand__dot"></span>
    <span class="brand__name">Tidewater<br>Holiday Park</span>
  </div>

  <p class="tagline">
    <span class="tagline__big">Reeling</span><span class="tagline__small">in the</span>
    <span class="tagline__second">views</span>
  </p>

  <h1 class="headline">
    <span class="headline__main">CABINS</span>
    <span class="headline__sub">AND CAMPING</span>
  </h1>

  <section class="facilities">
    <h2 class="facilities__title">FACILITIES</h2>
    <ul class="facilities__list">
      <li class="facilities__item">An Onsite Shop</li>
      <li class="facilities__item">Laundry</li>
      <li class="facilities__item">BBQ Facilities</li>
      <li class="facilities__item">Internet Access</li>
      <li class="facilities__item">Combined Kitchen /<br>Dining / TV Room</li>
      <li class="facilities__item">Petanque</li>
      <li class="facilities__item">Adventure Play-<br>ground</li>
      <li class="facilities__item">Caravan Storage</li>
      <li class="facilities__item">Local Cafés</li>
      <li class="facilities__item">Showers no charge</li>
    </ul>
  </section>

  <div class="social">
    <span class="social__label">follow us</span>
    <span class="social__mark social__mark--one"></span>
    <span class="social__mark social__mark--two"></span>
  </div>

  <address class="contact" style="font-style:normal">
    <div class="contact__line">64 9 555 0142
      <svg class="contact__icon" viewBox="0 0 20 20" aria-hidden="true"><path d="M5 2 L8 2 L9 6 L7 8 C8 10 10 12 12 13 L14 11 L18 12 L18 15 C18 17 16 18 14 18 C8 17 3 12 2 6 C2 4 3 2 5 2 Z" fill="var(--leaf-green)"/></svg>
    </div>
    <div class="contact__line">www.parkbookings.co
      <svg class="contact__icon" viewBox="0 0 20 20" aria-hidden="true"><g fill="none" stroke="var(--leaf-green)" stroke-width="1.8"><circle cx="10" cy="10" r="8"/><ellipse cx="10" cy="10" rx="3.5" ry="8"/><path d="M2 10 H18 M3.5 5.5 H16.5 M3.5 14.5 H16.5"/></g></svg>
    </div>
    <div class="contact__line">12 Harbour Lane Kauriwai Northland New Zealand
      <svg class="contact__icon" viewBox="0 0 20 20" aria-hidden="true"><path d="M10 1 C6 1 3.5 4 3.5 7.5 C3.5 12 10 19 10 19 C10 19 16.5 12 16.5 7.5 C16.5 4 14 1 10 1 Z M10 5 A2.5 2.5 0 1 1 10 10 A2.5 2.5 0 1 1 10 5 Z" fill="var(--leaf-green)" fill-rule="evenodd"/></svg>
    </div>
  </address>
</main>
</body>
</html>
```